Design of labels for exciting new natural skincare products...natural deodorant

I need some labels designed for a range of natural skincare, initially a natural deodorant paste. i will be offering a range of fragrances so i want a basic idea that i can drop different colours / ingredients into easily.

Fragrances are:
1. Jasmine, Orange and Bergamot
2. Lavender & Bergamot
3. Peppermint & Tea tree
4. Unscented
5. Lime, Lemongrass & Ginger

I am a new startup and will be selling online and through a couple of specialty online stores. The final design should encompass our ethos which is clean and green, not fussy nor clinical but friendly and easily accessible. I like fresh, contemporary modern look referencing vintage aesthetics.

The idea is that these products are better for your body AND the environment, and we pledge to use no plastic to package or distribute our products. i like the use of contemporary pastels such as soft pinks, tans and green/blue/aquas, though am open to new ideas too. the logo (attached) appears in red but that should not necessarily be used. i also like black and white with touches of colour.

Target Market(s)

Eco aware, health concious consumers with a reasonable skincare budget.

Industry/Entity Type

Skin Care Product

Font styles to use
Serif
Sans Serif
Decorative

Colors
2eb6a2
b768aa
eea4c8
fabb94
85cae6
cfeae6
eaf2ce
000000
eaeaea

Requirements
Must have
• Labels are for a small glass jar - the dimensions are 2cm high only and wrapping around the jar - at least 10cm wide. i'm also going to be providing a smaller size so this needs to be able to scale down to 1.5cm high and 8cm wide.
• the logo (supplied)
• title: Natural Deodorant
• Subtitle: Orange, Jasmine & Bergamot
• 45g
• Ingredients: tapioca starch*, bicarbonate of soda, Coconut oil*, shea butter*, mango butter*, diatomaceous earth*, sweet almond oil*, vitamin e*, tea tree oil*, Sweet orange essential oil*, Jasmine essential oil*, Bergamot essential oil*.
• *Certified organic ingredient
• (DESIGNERS - PLEASE NOTE NOT ALL THE INGREDIENTS ARE ORGANIC, PLEASE LIST THEM WITH A STAR * IF I HAVE SUPPLIED IT, THEN *Certified organic ingredient BELOW IN SLIGHTLY SMALLER TEXT - THIS SERVES AS THE KEY FOR THE INGREDIENTS LIST)
• wrenmeadow.nz
• Massage a pea-sized amount onto clean, dry armpits for an odour-free day.
• If irritation develops discontinue use and contact Wren Meadow. (please italicise the company name)
Nice to have
• open to ideas - i am attaching some examples of designs i like, you'll notice i swing between plain black and white aesthetics and a more decorative look. In general i like the old "medicine bottle" look, with hand sketched illustrations. But i'm open to ideas!

```html
<!DOCTYPE html>
<html lang="en">
<head>
<meta charset="utf-8">
<title>Wren Meadow – Natural Deodorant Label</title>
<link rel="stylesheet" href="https://fonts.googleapis.com/css2?family=Arimo:wght@400&family=Cookie&family=Josefin+Sans:wght@300;400&display=swap">
<style>
  :root {
    --page-bg: #e4e4e4;
    --label-bg: #d3d4d6;
    --band: #b768aa;
    --teal: #2eb6a2;
    --ink: #1f1f1f;
    --badge-green: #3f9a3f;
    --badge-dark: #2d2d2d;
    --white: #ffffff;
  }
  * { margin: 0; padding: 0; box-sizing: border-box; }
  html, body {
    width: 1200px; height: 887px; overflow: hidden;
    background: var(--page-bg);
  }
  .label {
    position: absolute; left: 0; top: 316px;
    width: 1200px; height: 255px;
    background: var(--label-bg);
    border-top: 9px solid var(--band);
    border-bottom: 9px solid var(--band);
    font-family: "Arimo", Arial, sans-serif;
    color: var(--ink);
  }
  .usage { position: absolute; left: 6px; top: 34px; width: 260px; }
  .usage-title { font-size: 18px; letter-spacing: 0.5px; }
  .usage-text { font-size: 15px; line-height: 19px; letter-spacing: 0.6px; }

  .brand-name {
    position: absolute; left: 0; width: 1144px; top: 22px;
    text-align: center;
    font-family: "Josefin Sans", sans-serif; font-weight: 400;
    font-size: 34px; color: var(--band);
  }
  .product-title {
    position: absolute; left: 0; width: 1150px; top: 100px;
    text-align: center;
    font-family: "Josefin Sans", sans-serif; font-weight: 300;
    font-size: 40px; letter-spacing: 1px; color: var(--teal);
  }
  .scent-bar {
    position: absolute; left: 450px; top: 146px; width: 250px; height: 23px;
    background: var(--band);
    font-family: "Cookie", cursive; font-size: 22px; line-height: 23px;
    color: var(--white); text-align: center;
  }
  .vegan-badge { position: absolute; left: 644px; top: 187px; }
  .net-weight {
    position: absolute; left: 0; width: 1144px; top: 227px;
    text-align: center; font-size: 16px;
  }
  .net-weight .divider { border-left: 1px solid var(--ink); margin: 0 3px; }

  .ingredients { position: absolute; left: 880px; top: 52px; width: 300px; }
  .ingredients-title {
    display: inline-block; font-size: 15px;
    border-bottom: 1px solid var(--ink); padding-bottom: 2px; margin-bottom: 6px;
  }
  .ingredients-list { font-size: 12px; line-height: 16.4px; }
  .certifications { position: absolute; left: 880px; top: 180px; }
</style>
</head>
<body>
  <section class="label">
    <div class="usage">
      <p class="usage-title">To use:</p>
      <p class="usage-text">For an odour-free day, massage a pea sized amount onto clean, dry underarms.</p>
    </div>

    <p class="brand-name">Wren Meadow</p>
    <h1 class="product-title">NATURAL DEODORANT</h1>
    <p class="scent-bar">Orange - Jasmine - Bergamot</p>

    <svg class="vegan-badge" width="44" height="40" viewBox="0 0 44 40" role="img" aria-label="Vegan certification badge">
      <circle cx="20" cy="20" r="18" fill="var(--badge-green)"/>
    </svg>

    <p class="net-weight">60ml<span class="divider"></span>20z</p>

    <div class="ingredients">
      <p class="ingredients-title">Ingredients :</p>
      <p class="ingredients-list">Coconut oil*, tapioca starch*, bicarbonate of soda, shea butter*, mango butter*, diatomaceous earth*, sweet almond oil*, vitamin e*, tea tree oil*, Sweet orange essential oil*, Jasmine essential oil*, Bergamot essential oil*.</p>
    </div>

    <svg class="certifications" width="260" height="56" viewBox="0 0 260 56">
      <g role="img" aria-label="Organic certification badge">
        <circle cx="30" cy="29" r="27" fill="none" stroke="var(--badge-green)" stroke-width="3"/>
        <circle cx="30" cy="29" r="20" fill="var(--badge-green)" opacity="0.25"/>
      </g>
      <rect x="70" y="6" width="52" height="46" rx="6" fill="var(--badge-dark)" opacity="0.2" role="img" aria-label="Not tested on animals badge"/>
      <circle cx="146" cy="29" r="27" fill="var(--badge-green)" role="img" aria-label="Recycling badge"/>
      <g role="img" aria-label="Period after opening icon">
        <rect x="206" y="22" width="40" height="28" rx="4" fill="none" stroke="var(--badge-dark)" stroke-width="1.5"/>
        <line x1="205" y1="17" x2="238" y2="2" stroke="var(--badge-dark)" stroke-width="2"/>
      </g>
    </svg>
  </section>
</body>
</html>
```